Best local air conditioning and heating contractor

We need a website design for a new company in Tampa Bay called the Summit Breeze Cooling Company. We provide superior services for residential and commercial properties as well as maintenance and installing HVAC systems. We also want to sell equipment, parts and filter on the website as well. We want it easy to use for customers. Rich with content and keywords for our area.

Target Market(s)

homeowners in Tampa Bay

Industry/Entity Type

HVAC air conditioning and heating

Coding

Coded - Design and coding required

Number of Pages Required

5+ page

Font styles to use
Sans Serif

Requirements
Nice to have
• would like the colors to be same as logo

```html
<!DOCTYPE html>
<html lang="en">
<head>
<meta charset="utf-8">
<title>Summit Breeze Cooling Company</title>
<link href="https://fonts.googleapis.com/css2?family=Poppins:wght@300;400;500;600;700&family=Oswald:wght@300;500;600&display=swap" rel="stylesheet">
<style>
:root{
  --navy:#22306b;
  --navy-dark:#1b2658;
  --red:#d9242a;
  --red-dark:#b81d22;
  --gray:#f3f3f3;
  --text:#3a3a3a;
  --white:#ffffff;
}
*{margin:0;padding:0;box-sizing:border-box}
html,body{width:1200px;height:4515px;overflow:hidden}
body{position:relative;font-family:'Poppins',sans-serif;color:var(--text);background:var(--white)}
.abs{position:absolute}
a{color:inherit;text-decoration:none}
.btn{position:absolute;display:flex;align-items:center;justify-content:center;gap:10px;border-radius:30px;color:var(--white);font-size:14px;font-weight:500;text-transform:uppercase}
.btn svg{width:16px;height:12px}
.btn-red{background:var(--red)}
.btn-navy{background:var(--navy)}
.photo{position:absolute}

/* header */
.brand{position:absolute;left:74px;top:46px;width:250px;display:flex;align-items:center;gap:10px;color:var(--navy);font-weight:700;font-size:19px;line-height:1.15;text-transform:uppercase}
.brand-dot{flex:none;width:18px;height:18px;border-radius:50%;background:var(--red)}
.topbar{position:absolute;left:459px;top:30px;display:flex;gap:18px;font-size:13px;color:#333}
.topbar span{display:flex;align-items:center;gap:8px}
.topicon{width:26px;height:26px;border:2px solid var(--red);border-radius:5px;display:flex;align-items:center;justify-content:center}
.topline{position:absolute;left:459px;top:75px;width:666px;height:2px;background:var(--red)}
.nav{position:absolute;top:103px;left:459px;font-size:13px;color:#444}
.nav a{position:absolute;white-space:nowrap;top:0}
.nav .active{color:var(--navy);font-weight:600}
.header-icons{position:absolute;top:26px;left:1010px;display:flex;gap:18px}
.badge{position:absolute;left:1032px;top:22px;width:14px;height:14px;border-radius:50%;background:var(--red);color:#fff;font-size:9px;text-align:center;line-height:14px}

/* hero */
.hero{position:absolute;left:0;top:172px;width:1200px;height:753px;background:var(--navy);overflow:hidden}
.hero-photo{position:absolute;inset:0;background:linear-gradient(135deg,#c9ccd0 0%,#e6e3dc 40%,#b9c0c7 70%,#7f8a96 100%);clip-path:polygon(420px 0,1200px 0,1200px 753px,596px 753px)}
.hero-stripe{position:absolute;inset:0;background:var(--red);clip-path:polygon(403px 0,420px 0,596px 753px,587px 753px)}
.hero h1{position:absolute;left:79px;top:288px;font-family:'Oswald',sans-serif;line-height:1;text-transform:uppercase}
.hero h1 .a{display:block;color:var(--red);font-size:56px;font-weight:600}
.hero h1 .b{display:block;color:var(--white);font-size:50px;font-weight:300;margin-top:8px}
.hero p{position:absolute;left:79px;top:416px;width:360px;color:var(--white);font-size:13px;line-height:1.75}

/* services strip */
.strip{position:absolute;left:0;top:1034px;width:1200px;height:1003px;background:var(--gray)}
.scard{position:absolute;top:1027px;width:338px;height:138px;background:var(--white);box-shadow:0 4px 14px rgba(0,0,0,.06);display:flex;align-items:center;padding-left:24px;gap:20px}
.scard h3{font-size:17px;font-weight:500;color:var(--navy);text-transform:uppercase;margin-bottom:8px}
.scard p{font-size:12.5px;line-height:1.7;color:#555}
.scard svg{flex:none;width:60px;height:60px}
.scard.hot{background:var(--red)}
.scard.hot h3,.scard.hot p{color:var(--white)}

/* about */
.about-frame{position:absolute;left:70px;top:1354px;width:496px;height:524px;background:var(--red)}
.about-photo{left:84px;top:1337px;width:505px;height:527px;background:linear-gradient(160deg,#d9d2c2,#b9b3a6 55%,#8d8a86)}
.kicker{position:absolute;font-family:'Oswald',sans-serif;font-weight:500;color:var(--red);font-size:22px;text-transform:uppercase;display:flex;align-items:center;gap:12px}
.kicker i{display:block;width:36px;height:2px;background:var(--red)}
.about h2{position:absolute;left:681px;top:1417px;width:460px;font-size:31px;font-weight:600;line-height:1.38;color:var(--navy)}
.about p{position:absolute;left:681px;top:1581px;width:435px;font-size:13px;line-height:1.75;color:#444}

/* our services */
.sec-title{position:absolute;left:0;width:1200px;text-align:center;font-size:37px;font-weight:600;line-height:1.2;color:var(--navy)}
.card{position:absolute;top:2328px;width:310px;height:391px;background:var(--white);box-shadow:0 3px 14px rgba(0,0,0,.12);text-align:center}
.card.active{border:2px solid var(--red);height:423px}
.card .img{position:absolute;left:7px;top:7px;right:7px;height:210px}
.card .ico{position:absolute;left:50%;top:185px;width:62px;height:62px;margin-left:-31px}
.card h3{position:absolute;left:0;right:0;top:258px;font-size:18px;font-weight:600;line-height:1.2;color:var(--navy);text-transform:uppercase}
.card p{position:absolute;left:30px;right:30px;top:312px;font-size:14px;line-height:1.75;color:#555}
.card .more{position:absolute;left:0;right:0;top:378px;font-size:13px;font-weight:500;color:var(--red);text-transform:uppercase}

/* banner */
.banner{position:absolute;left:0;top:2984px;width:1200px;height:418px;overflow:hidden}
.banner-photo{inset:0;background:linear-gradient(100deg,#d7d7d3,#bfc1c0 45%,#e4e3de 70%)}
.banner-red{position:absolute;inset:0;background:var(--red);clip-path:polygon(780px 0,1200px 0,1200px 418px,795px 418px,634px 222px)}
.banner-shade{position:absolute;inset:0;background:var(--red-dark);clip-path:polygon(780px 0,830px 0,680px 222px,634px 222px)}
.banner h2{position:absolute;right:79px;top:102px;text-align:right;font-family:'Oswald',sans-serif;font-weight:500;font-size:42px;line-height:1.4;color:var(--white);text-transform:uppercase}
.banner p{position:absolute;right:79px;top:262px;width:320px;text-align:right;font-size:13px;line-height:1.7;color:var(--white)}

/* reviews */
.reviews-bg{left:0;top:3402px;width:1200px;height:724px;background:linear-gradient(180deg,#ffffff,#f4eeea 50%,#f7f3f0)}
.review{position:absolute;top:3691px;width:439px;height:290px;border-radius:30px 60px 30px 30px;color:var(--white);padding:110px 38px 0 33px;font-size:13px;line-height:1.75}
.review.red{left:144px;background:var(--red)}
.review.navy{left:617px;background:var(--navy)}
.avatar{position:absolute;width:98px;height:98px;border-radius:50%;border:4px solid var(--white);background:linear-gradient(180deg,#d8d8d8,#9a9a9a)}
.rname{position:absolute;font-size:16px;font-weight:500;color:var(--white)}
.stars{position:absolute;color:#ffd23a;font-size:12px;letter-spacing:1px}
.quote{position:absolute;font-family:'Oswald',sans-serif;font-size:64px;font-weight:600;color:var(--white);line-height:1}
.dots{position:absolute;left:556px;top:4040px;display:flex;gap:8px}
.dots i{width:12px;height:12px;border-radius:50%;border:1.5px solid var(--navy)}
.dots i.on{background:var(--navy)}

/* footer */
.footer{position:absolute;left:0;top:4126px;width:1200px;height:324px;background:var(--navy);color:var(--white)}
.footer .brand{color:var(--white);left:88px;top:70px}
.fdiv{position:absolute;top:79px;width:1px;height:201px;background:rgba(255,255,255,.25)}
.fdiv::before{content:"";position:absolute;left:-4px;top:0;width:9px;height:9px;border-radius:50%;background:var(--red)}
.footer h4{position:absolute;font-size:17px;font-weight:500;text-transform:uppercase}
.flinks{position:absolute;left:412px;top:150px;list-style:none;font-size:12.5px;line-height:27px;text-transform:uppercase}
.fcontact{position:absolute;left:625px;display:flex;gap:20px;font-size:12.5px;line-height:1.3}
.fcontact .ic{flex:none;width:26px;height:26px;border:1px solid rgba(255,255,255,.6);border-radius:4px;display:flex;align-items:center;justify-content:center}
.news-input{position:absolute;left:920px;top:221px;width:210px;height:32px;border:1.5px solid var(--red);border-radius:18px;background:var(--white);font-size:11px;color:#888;padding:8px 16px}
.copy{position:absolute;left:0;top:4450px;width:1200px;height:65px;background:var(--red);color:var(--white);font-size:11.5px;text-align:center;line-height:65px}
</style>
</head>
<body>

<header>
  <div class="brand"><span class="brand-dot"></span><span>Summit Breeze Cooling Company</span></div>
  <div class="topbar">
    <span><i class="topicon"><svg width="14" height="14" viewBox="0 0 24 24"><path fill="#d9242a" d="M6.6 10.8a15 15 0 006.6 6.6l2.2-2.2c.3-.3.7-.4 1-.2 1.1.4 2.3.6 3.6.6.6 0 1 .4 1 1V20c0 .6-.4 1-1 1A17 17 0 013 4c0-.6.4-1 1-1h3.5c.6 0 1 .4 1 1 0 1.3.2 2.5.6 3.6.1.3 0 .7-.2 1z"/></svg></i>1-555-010-2020</span>
    <span><i class="topicon" style="background:var(--red)"><svg width="14" height="12" viewBox="0 0 24 20"><rect x="1" y="2" width="22" height="16" rx="2" fill="none" stroke="#fff" stroke-width="2"/><path d="M2 3l10 8 10-8" fill="none" stroke="#fff" stroke-width="2"/></svg></i>hello@summitbreeze.example</span>
  </div>
  <div class="header-icons">
    <svg width="24" height="22" viewBox="0 0 24 22"><path d="M1 2h4l3 12h12l3-9H7" fill="none" stroke="#22306b" stroke-width="2.4"/><circle cx="9" cy="19" r="2" fill="#22306b"/><circle cx="18" cy="19" r="2" fill="#22306b"/></svg>
    <svg width="20" height="22" viewBox="0 0 20 22"><circle cx="10" cy="6" r="5" fill="#22306b"/><path d="M0 22c0-6 4-9 10-9s10 3 10 9z" fill="#22306b"/></svg>
    <svg width="22" height="22" viewBox="0 0 22 22"><circle cx="9" cy="9" r="7" fill="none" stroke="#22306b" stroke-width="2"/><path d="M14 14l6 6" stroke="#22306b" stroke-width="2"/></svg>
  </div>
  <span class="badge">0</span>
  <div class="topline"></div>
  <nav class="nav">
    <a class="active" style="left:0">HOME</a>
    <a style="left:79px">ABOUT US</a>
    <a style="left:184px">SERVICES</a>
    <a style="left:284px">PRODUCTS</a>
    <a style="left:394px">REVIEWS</a>
    <a style="left:490px">BLOG</a>
  </nav>
  <a class="btn btn-red" style="left:1007px;top:91px;width:116px;height:40px;font-size:13px;font-weight:400">Contact Us</a>
</header>

<section class="hero">
  <div class="hero-photo" role="img" aria-label="Technician in a yellow hard hat carrying an outdoor air conditioning unit"></div>
  <div class="hero-stripe"></div>
  <h1><span class="a">Cool Solutions</span><span class="b">For House &amp; Office</span></h1>
  <p>Lorem ipsum dolor sit amet, consectetur adipiscing elit, sed do eiusmod tempor incididunt ut labore et</p>
  <a class="btn btn-red" style="left:79px;top:518px;width:171px;height:53px;font-size:15px;font-weight:400">Contact Us <svg viewBox="0 0 16 12"><path d="M0 6h14M9 1l5 5-5 5" fill="none" stroke="#fff" stroke-width="1.8"/></svg></a>
</section>

<div class="strip"></div>
<div class="scard" style="left:75px">
  <svg viewBox="0 0 60 60"><rect x="4" y="8" width="52" height="22" rx="3" fill="none" stroke="#d9242a" stroke-width="2.5"/><path d="M10 22h40" stroke="#d9242a" stroke-width="2"/><circle cx="20" cy="42" r="9" fill="none" stroke="#d9242a" stroke-width="2.5"/><path d="M20 33v18M11 42h18" stroke="#d9242a" stroke-width="2"/><path d="M36 36q3 4 0 8q-3 4 0 8M44 36q3 4 0 8q-3 4 0 8" fill="none" stroke="#d9242a" stroke-width="2"/></svg>
  <div><h3>Air Conditioning</h3><p>Lorem ipsum dolor sit amet,<br>consectetur adipiscing elit,</p></div>
</div>
<div class="scard hot" style="left:433px">
  <svg viewBox="0 0 60 60"><rect x="12" y="4" width="36" height="52" rx="18" fill="none" stroke="#fff" stroke-width="2.5"/><path d="M18 22h24M16 30h28M16 38h28M18 46h24" stroke="#fff" stroke-width="2.5"/><circle cx="30" cy="13" r="3" fill="#fff"/></svg>
  <div><h3>Heating Systems</h3><p>Lorem ipsum dolor sit amet,<br>consectetur adipiscing elit,</p></div>
</div>
<div class="scard" style="left:783px">
  <svg viewBox="0 0 60 60"><rect x="8" y="8" width="44" height="44" rx="5" fill="none" stroke="#d9242a" stroke-width="2.5"/><circle cx="30" cy="30" r="16" fill="none" stroke="#d9242a" stroke-width="2.5"/><path d="M30 30q-2-10 6-12M30 30q10 0 10 8M30 30q-8 6-14-1" fill="none" stroke="#d9242a" stroke-width="2.5"/><circle cx="30" cy="30" r="3" fill="#d9242a"/></svg>
  <div><h3>Air Ventilation</h3><p>Lorem ipsum dolor sit amet,<br>consectetur adipiscing elit,</p></div>
</div>

<section class="about">
  <div class="about-frame"></div>
  <div class="photo about-photo" role="img" aria-label="Technician servicing a wall-mounted outdoor air conditioning unit"></div>
  <div class="kicker" style="left:681px;top:1377px">About Us <i></i></div>
  <h2>We Create The Right Climate And Temperature For Your Home</h2>
  <p>Lorem ipsum dolor sit amet, consectetur adipiscing elit, sed do eiusmod tempor incididunt ut labore et dolore magna aliqua. Quis ipsum suspendisse ultrices gravida. Risus commodo viverra maecenas accumsan lacus vel facilisis.</p>
  <a class="btn btn-navy" style="left:681px;top:1726px;width:148px;height:44px;font-size:13px;font-weight:400">Know More <svg viewBox="0 0 16 12"><path d="M0 6h14M9 1l5 5-5 5" fill="none" stroke="#fff" stroke-width="1.8"/></svg></a>
</section>

<section class="services">
  <div class="kicker" style="left:487px;top:2122px"><i></i>Our Services<i></i></div>
  <h2 class="sec-title" style="top:2174px">We provide a full range services for<br>your home</h2>

  <div class="card" style="left:96px">
    <div class="img" role="img" aria-label="Two technicians installing an outdoor air conditioning unit" style="background:linear-gradient(135deg,#d6d4cf,#a9aeb4 60%,#5d6a86)"></div>
    <svg class="ico" viewBox="0 0 62 62"><path d="M31 2l26 12v20c0 14-12 22-26 26C17 56 5 48 5 34V14z" fill="#d9242a"/><rect x="19" y="22" width="24" height="12" rx="2" fill="none" stroke="#fff" stroke-width="2"/><path d="M23 38q2 3 0 6M31 38q2 3 0 6M39 38q2 3 0 6" stroke="#fff" stroke-width="2" fill="none"/></svg>
    <h3>Air Conditioning<br>Installation</h3>
    <p>Lorem ipsum dolor sit amet, consectetur adipiscing elit</p>
  </div>
  <div class="card active" style="left:452px">
    <div class="img" role="img" aria-label="Technician on a ladder repairing an air conditioning unit" style="background:linear-gradient(135deg,#cfcbc3,#ece8e0 50%,#9ea3a8)"></div>
    <svg class="ico" viewBox="0 0 62 62"><path d="M31 2l26 12v20c0 14-12 22-26 26C17 56 5 48 5 34V14z" fill="#d9242a"/><circle cx="31" cy="31" r="11" fill="none" stroke="#fff" stroke-width="2"/><circle cx="31" cy="31" r="4" fill="#fff"/><path d="M31 16v5M31 41v5M16 31h5M41 31h5" stroke="#fff" stroke-width="2"/></svg>
    <h3>Air Conditioning<br>Repair</h3>
    <p>Lorem ipsum dolor sit amet, consectetur adipiscing elit</p>
    <a class="more">Read More &rarr;</a>
  </div>
  <div class="card" style="left:802px">
    <div class="img" role="img" aria-label="Two technicians in helmets installing a ceiling HVAC system" style="background:linear-gradient(135deg,#e2e3e5,#b7bcc4 50%,#3d5292)"></div>
    <svg class="ico" viewBox="0 0 62 62"><path d="M31 2l26 12v20c0 14-12 22-26 26C17 56 5 48 5 34V14z" fill="#d9242a"/><path d="M31 16v30M18 23l26 16M44 23L18 39" stroke="#fff" stroke-width="2.2"/><circle cx="31" cy="31" r="4" fill="#fff"/></svg>
    <h3>Installing HVAC<br>Systems</h3>
    <p>Lorem ipsum dolor sit amet, consectetur adipiscing elit</p>
  </div>

  <a class="btn btn-navy" style="left:503px;top:2810px;width:194px;height:46px;font-size:13px;font-weight:400">View All Services <svg viewBox="0 0 16 12"><path d="M0 6h14M9 1l5 5-5 5" fill="none" stroke="#fff" stroke-width="1.8"/></svg></a>
</section>

<section class="banner">
  <div class="photo banner-photo" role="img" aria-label="Technician with a drill beside an outdoor air conditioning unit against a concrete wall"></div>
  <div class="banner-red"></div>
  <div class="banner-shade"></div>
  <h2>The Temperature Of<br>Cooling Is In Your Hand</h2>
  <p>Lorem ipsum dolor sit amet, consectetur adipiscing elit, sed do eiusmod tempor incidi</p>
  <a class="btn btn-navy" style="left:977px;top:322px;width:144px;height:42px;font-size:13px;font-weight:400">Contact Us <svg viewBox="0 0 16 12"><path d="M0 6h14M9 1l5 5-5 5" fill="none" stroke="#fff" stroke-width="1.8"/></svg></a>
</section>

<section class="reviews">
  <div class="photo reviews-bg" role="img" aria-label="Soft faded background of a relaxed family at home"></div>
  <div class="kicker" style="left:488px;top:3522px"><i></i>Client Reviews<i></i></div>
  <h2 class="sec-title" style="top:3568px">What our customers say</h2>

  <div class="review red">Lorem ipsum dolor sit amet, consectetur adipiscing elit. Sed vitae lobortis libero, at ultricies odio. Suspendisse vel sem in turpis tempus pretium. Etiam iaculis tortor sed egestas porttitor. Curabitur molestie pretium leo, quis sollicitudin nisi feugiat efficitur.</div>
  <div class="avatar" role="img" aria-label="Customer portrait" style="left:141px;top:3658px"></div>
  <div class="rname" style="left:259px;top:3708px">Marcus Reed</div>
  <div class="stars" style="left:259px;top:3732px">★★★★★</div>
  <div class="quote" style="left:496px;top:3708px">&#8221;</div>

  <div class="review navy">Lorem ipsum dolor sit amet, consectetur adipiscing elit. Sed vitae lobortis libero, at ultricies odio. Suspendisse vel sem in turpis tempus pretium. Etiam iaculis tortor sed egestas porttitor. Curabitur molestie pretium leo, quis sollicitudin nisi feugiat efficitur.</div>
  <div class="avatar" role="img" aria-label="Customer portrait" style="left:617px;top:3658px"></div>
  <div class="rname" style="left:731px;top:3708px">Daniel Hayes</div>
  <div class="stars" style="left:731px;top:3732px">★★★★★</div>
  <div class="quote" style="left:968px;top:3708px">&#8221;</div>

  <svg class="abs" style="left:70px;top:3848px" width="20" height="40" viewBox="0 0 20 40"><path d="M18 2L2 20l16 18" fill="none" stroke="#22306b" stroke-width="1.6"/></svg>
  <svg class="abs" style="left:1096px;top:3848px" width="20" height="40" viewBox="0 0 20 40"><path d="M2 2l16 18L2 38" fill="none" stroke="#22306b" stroke-width="1.6"/></svg>
  <div class="dots"><i></i><i></i><i class="on"></i><i></i></div>
</section>

<footer class="footer">
  <div class="brand"><span class="brand-dot"></span><span>Summit Breeze Cooling Company</span></div>
  <p class="abs" style="left:83px;top:206px;width:240px;font-size:12.5px;line-height:1.75">Lorem ipsum dolor sit amet, con sectetur adipiscing elit sed do</p>

  <div class="fdiv" style="left:378px"></div>
  <h4 style="left:406px;top:93px">Quick Links</h4>
  <ul class="flinks"><li>About Us</li><li>Services</li><li>Products</li><li>Blog</li><li>Contact Us</li></ul>

  <div class="fdiv" style="left:594px"></div>
  <h4 style="left:625px;top:95px">Contact Us</h4>
  <div class="fcontact" style="top:146px"><span class="ic"><svg width="12" height="12" viewBox="0 0 24 24"><path fill="#fff" d="M6.6 10.8a15 15 0 006.6 6.6l2.2-2.2c.3-.3.7-.4 1-.2 1.1.4 2.3.6 3.6.6.6 0 1 .4 1 1V20c0 .6-.4 1-1 1A17 17 0 013 4c0-.6.4-1 1-1h3.5c.6 0 1 .4 1 1 0 1.3.2 2.5.6 3.6.1.3 0 .7-.2 1z"/></svg></span><span>CALL US<br>555 210 4433</span></div>
  <div class="fcontact" style="top:196px"><span class="ic"><svg width="12" height="10" viewBox="0 0 24 20"><rect x="1" y="2" width="22" height="16" rx="2" fill="#fff"/><path d="M2 3l10 8 10-8" fill="none" stroke="#22306b" stroke-width="2"/></svg></span><span>EMAIL US<br>hello@summitbreeze.example</span></div>
  <div class="fcontact" style="top:246px"><span class="ic"><svg width="10" height="14" viewBox="0 0 20 28"><path d="M10 0a10 10 0 0110 10c0 7-10 18-10 18S0 17 0 10A10 10 0 0110 0z" fill="#fff"/><circle cx="10" cy="10" r="4" fill="#22306b"/></svg></span><span>Address line Dummy Here<br>Address line Here</span></div>

  <div class="fdiv" style="left:893px"></div>
  <h4 style="left:923px;top:101px">Newsletter Sign Up</h4>
  <p class="abs" style="left:928px;top:158px;width:220px;font-size:12.5px;line-height:1.5">Subscribe our newsletter to get the latest news.</p>
  <div class="news-input">Enter Email Address</div>
  <svg class="abs" style="left:1096px;top:227px" width="22" height="22" viewBox="0 0 22 22"><circle cx="11" cy="11" r="10" fill="none" stroke="#d9242a" stroke-width="1.4"/><path d="M6 11h9M12 7l4 4-4 4" fill="none" stroke="#d9242a" stroke-width="1.4"/></svg>
</footer>
<div class="copy">Copyright © 2024 All Rights Reserved By Summit Breeze Cooling Company</div>

</body>
</html>
```